Plakat-Design für eine Werbeschild für ein Geflügelhof
Zielgruppe
Wir sind ein Geflügelhof, Landhandel, Hofladen, Eier stehen seit über 100 Jahren für Hof Kranwede, artgerechte Tierhaltung und Artikelvielfalt machen uns bekannt.
Aufgabenstellung
Das Werbeschild wird auf dem Hof aufgestellt und soll den Weg zum Hof zeigen.
- die Maße vom Schild: 1,50m breit x 2,40m hoch
- Grafiken werden als .ai und .pdf benötigt
- Logo ist hochgelagen
- Foto von unserer Vorstellung ist hochgeladen
Das Schild muss 400 m RECHTS drauf gedruckt haben.
Falls es zu breit wäre, könnte das Logo ja vielleicht auch über Hof Kranwede.
Das ganze wird bei plattenwerk auf eine MetoxPan-Platte in den Druck gegeben.

```html
<!DOCTYPE html>
<html lang="de">
<head>
<meta charset="UTF-8">
<title>Hof Kranwede – Wegweiser</title>
<link href="https://fonts.googleapis.com/css2?family=Patrick+Hand&family=Roboto:wght@700&display=swap" rel="stylesheet">
<style>
  :root {
    --farm-green: #2e6e3a;
    --farm-green-soft: #e6efe7;
    --signal-red: #c41f27;
    --paper: #ffffff;
  }
  * { margin: 0; padding: 0; box-sizing: border-box; }
  html, body {
    width: 857px;
    height: 1200px;
    overflow: hidden;
    background: var(--paper);
  }
  .sign {
    position: absolute;
    left: 140px;
    top: 143px;
    width: 558px;
    height: 884px;
    background: var(--paper);
    overflow: hidden;
  }
  .brand {
    position: absolute;
    left: 40px;
    top: 57px;
    display: flex;
    align-items: center;
    gap: 16px;
  }
  .brand-mark {
    width: 87px;
    height: 87px;
    border-radius: 50%;
    background: var(--farm-green);
    flex: none;
  }
  .brand-name {
    font-family: "Roboto", Arial, sans-serif;
    font-weight: 700;
    font-size: 54px;
    color: var(--farm-green);
    letter-spacing: 0.5px;
    white-space: nowrap;
  }
  .headline {
    position: absolute;
    left: 0;
    top: 200px;
    width: 100%;
    text-align: center;
    font-family: "Patrick Hand", "Comic Sans MS", cursive;
    font-weight: 400;
    font-size: 86px;
    line-height: 119px;
    color: var(--farm-green);
  }
  .headline-line {
    display: block;
    white-space: nowrap;
  }
  .direction-band {
    position: absolute;
    left: 0;
    top: 452px;
    width: 100%;
    height: 167px;
    background: var(--signal-red);
    display: flex;
    align-items: center;
    justify-content: center;
  }
  .direction-text {
    font-family: "Roboto", Arial, sans-serif;
    font-weight: 700;
    font-size: 76px;
    color: var(--paper);
    letter-spacing: 0.5px;
    white-space: nowrap;
  }
  .farm-animals {
    position: absolute;
    left: 0;
    top: 619px;
    width: 100%;
    height: 206px;
    background: linear-gradient(to bottom, var(--paper), var(--farm-green-soft));
  }
  .meadow {
    position: absolute;
    left: 0;
    top: 825px;
    width: 100%;
    height: 59px;
    background: var(--farm-green);
  }
</style>
</head>
<body>
  <main class="sign">
    <header class="brand">
      <div class="brand-mark"></div>
      <span class="brand-name">Hof Kranwede</span>
    </header>

    <h1 class="headline">
      <span class="headline-line">Einkauf auf</span>
      <span class="headline-line">dem Bauernhof</span>
    </h1>

    <section class="direction-band">
      <p class="direction-text">400M RECHTS</p>
    </section>

    <div class="farm-animals" role="img" aria-label="Grüne Silhouetten eines Huhns und einer Ente, die sich auf einer Wiese gegenüberstehen"></div>
    <div class="meadow"></div>
  </main>
</body>
</html>
```